Stationery Design Project

We need a stationery design for a new business consulting business based in New Zealand.
We have the logo and business cards designed and we're looking for letterhead, compliments slip and PowerPoint presentation format that aligns with our business cards.
Industry/Entity Type
Business
Requirements
Must have
- same colors and format as business cards

```html
<!DOCTYPE html>
<html lang="en">
<head>
<meta charset="utf-8">
<title>Kereru Advisory Stationery</title>
<link href="https://fonts.googleapis.com/css2?family=Questrial&display=swap" rel="stylesheet">
<style>
  :root {
    --backdrop: #6f6f6f;
    --paper-top: #ffffff;
    --paper-bottom: #e9e9e9;
    --brand-green: #8cc63f;
    --brand-grey: #5e5e5e;
    --side-grey: #9a9a9a;
    --ink: #333333;
    --white: #ffffff;
  }
  * { margin: 0; padding: 0; box-sizing: border-box; }
  html, body { width: 1200px; height: 1051px; overflow: hidden; }
  body {
    position: relative;
    background: var(--backdrop);
    font-family: "Questrial", "Century Gothic", sans-serif;
    color: var(--ink);
  }
  .sheet {
    position: absolute;
    background: linear-gradient(180deg, var(--paper-top) 45%, var(--paper-bottom) 100%);
  }
  .letterhead { left: 59px; top: 27px; width: 764px; height: 989px; }
  .comp-slip { left: 399px; top: 417px; width: 744px; height: 356px; }
  .accent-bar { position: absolute; top: 0; right: 0; background: var(--brand-green); }
  .letterhead .accent-bar { left: 189px; height: 17px; }
  .comp-slip .accent-bar { left: 188px; height: 19px; }
  .side-bar { position: absolute; left: 0; bottom: 0; width: 18px; background: var(--side-grey); }
  .letterhead .side-bar { top: 120px; }
  .comp-slip .side-bar { top: 116px; }

  .brand {
    position: absolute;
    display: flex;
    align-items: center;
    gap: 10px;
    font-size: 44px;
    line-height: 1;
    color: var(--brand-grey);
    letter-spacing: -0.5px;
    white-space: nowrap;
  }
  .brand-dot { width: 16px; height: 16px; border-radius: 50%; background: var(--brand-green); flex: none; }
  .letterhead .brand { left: 54px; top: 74px; }
  .comp-slip .brand { left: 52px; top: 62px; font-size: 42px; }

  .contact {
    position: absolute;
    font-size: 10.5px;
    line-height: 12.5px;
    list-style: none;
  }
  .contact li { display: flex; align-items: center; gap: 5px; }
  .contact svg { width: 8px; height: 8px; flex: none; }
  .contact .plain { padding-left: 0; }
  .letterhead .contact { left: 553px; top: 890px; }
  .comp-slip .contact { left: 530px; top: 46px; }
  .contact strong { font-weight: normal; color: #111; }

  .compliments {
    position: absolute;
    left: 530px; top: 325px;
    font-size: 16px;
    color: var(--brand-green);
    font-variant: small-caps;
    letter-spacing: 0.3px;
  }

  .brand-display {
    position: absolute;
    left: 915px; top: 960px;
    color: var(--white);
    font-size: 38px;
  }
</style>
</head>
<body>

<section class="sheet letterhead" aria-label="Letterhead">
  <div class="accent-bar"></div>
  <div class="side-bar"></div>
  <div class="brand"><span class="brand-dot"></span>Kereru Advisory</div>
  <ul class="contact">
    <li>PO Box 418203</li>
    <li>Wellington 6140 New Zealand</li>
    <li><svg viewBox="0 0 10 10"><path d="M2 1l2 2-1 1.2a6 6 0 0 0 2.8 2.8L7 6l2 2-1.4 1.5C4.5 9.5.5 5.5.5 2.4z" fill="var(--brand-green)"/></svg>+ 64 21 555 0198</li>
    <li><svg viewBox="0 0 10 10"><rect x="0.7" y="2" width="8.6" height="6" fill="none" stroke="var(--brand-green)" stroke-width="1"/><path d="M0.7 2L5 5.5 9.3 2" fill="none" stroke="var(--brand-green)" stroke-width="1"/></svg>hello@kereruadvisory.com</li>
    <li><svg viewBox="0 0 10 10"><circle cx="5" cy="5" r="4.3" fill="var(--brand-green)"/><path d="M3 5h4M5 3l2 2-2 2" fill="none" stroke="#fff" stroke-width="1"/></svg>www.kereruadvisory.com</li>
  </ul>
</section>

<section class="sheet comp-slip" aria-label="Compliments slip">
  <div class="accent-bar"></div>
  <div class="side-bar"></div>
  <div class="brand"><span class="brand-dot"></span>Kereru Advisory</div>
  <ul class="contact">
    <li>PO Box 418203</li>
    <li>Wellington 6140 New Zealand</li>
    <li><svg viewBox="0 0 10 10"><path d="M2 1l2 2-1 1.2a6 6 0 0 0 2.8 2.8L7 6l2 2-1.4 1.5C4.5 9.5.5 5.5.5 2.4z" fill="var(--brand-green)"/></svg>+ 64 21 555 0198</li>
    <li><svg viewBox="0 0 10 10"><rect x="0.7" y="2" width="8.6" height="6" fill="none" stroke="var(--brand-green)" stroke-width="1"/><path d="M0.7 2L5 5.5 9.3 2" fill="none" stroke="var(--brand-green)" stroke-width="1"/></svg>hello@kereruadvisory.com</li>
    <li><svg viewBox="0 0 10 10"><circle cx="5" cy="5" r="4.3" fill="var(--brand-green)"/><path d="M3 5h4M5 3l2 2-2 2" fill="none" stroke="#fff" stroke-width="1"/></svg><span>www.<strong>kereruadvisory</strong>.com</span></li>
  </ul>
  <p class="compliments">With Compliments</p>
</section>

<div class="brand-display">Kereru Advisory</div>

</body>
</html>
```